Regional Job Board needs a powerpoint design

Looking for a powerful design for a new company in Cheshire, UK.
Our product is a job board that is targeted at local job seekers and employers within a certain region's of the UK.
The theme is Local people for Local Jobs, the Website is feature rich with job board technology, so looking to use the powerpoint to communicate screen shots and features across the presentation, including a strong education and community theme to support the feel. Modern, professional, colourful,

It Company

```html
<!DOCTYPE html>
<html lang="en">
<head>
<meta charset="utf-8">
<title>Agenda Slide</title>
<link rel="stylesheet" href="https://fonts.googleapis.com/css2?family=Roboto:wght@400;500;700&display=swap">
<style>
  :root {
    --header-blue: #1185c1;
    --footer-blue: #0c6cb5;
    --heading-blue: #1a6fb8;
    --item-blue: #3399cc;
    --bullet-orange: #f08a24;
    --muted-grey: #9a9a9a;
    --body-grey: #8a8a8a;
    --white: #ffffff;
  }
  * { margin: 0; padding: 0; box-sizing: border-box; }
  html, body {
    width: 1200px;
    height: 900px;
    overflow: hidden;
    background: var(--white);
    font-family: "Roboto", Arial, sans-serif;
  }
  .slide {
    position: relative;
    width: 1200px;
    height: 900px;
    background: var(--white);
  }
  .slide-header {
    position: absolute;
    top: 0; left: 0;
    width: 1200px;
    height: 102px;
    background: var(--header-blue);
    display: flex;
    align-items: center;
    justify-content: space-between;
    padding: 0 22px 0 30px;
  }
  .slide-title {
    color: var(--white);
    font-size: 39px;
    font-weight: 700;
    letter-spacing: -0.3px;
  }
  .brand {
    display: flex;
    align-items: center;
    gap: 10px;
    color: var(--white);
    font-size: 28px;
    font-weight: 700;
  }
  .brand-dot {
    width: 30px;
    height: 30px;
    border-radius: 50%;
    background: var(--white);
  }
  .content {
    position: absolute;
    top: 180px;
    left: 87px;
    width: 1040px;
  }
  .section-heading {
    font-size: 27px;
    font-weight: 700;
    color: var(--heading-blue);
    line-height: 36px;
  }
  .section-heading .accent { color: var(--muted-grey); }
  .section-subtext {
    margin-top: 10px;
    font-size: 20.5px;
    line-height: 30px;
    color: var(--body-grey);
  }
  .agenda-list {
    list-style: none;
    margin-top: 32px;
    margin-left: -3px;
  }
  .agenda-item {
    display: flex;
    align-items: center;
    height: 63px;
    font-size: 21px;
    font-weight: 700;
    color: var(--item-blue);
  }
  .agenda-bullet {
    flex: 0 0 34px;
    width: 34px;
    height: 34px;
    margin-right: 16px;
  }
  .slide-footer {
    position: absolute;
    left: 0; bottom: 0;
    width: 1200px;
    height: 39px;
    background: var(--footer-blue);
    display: flex;
    align-items: center;
    justify-content: flex-end;
    padding-right: 16px;
    color: var(--white);
    font-size: 16px;
  }
</style>
</head>
<body>
  <div class="slide">
    <header class="slide-header">
      <h1 class="slide-title">Agenda Slide</h1>
      <div class="brand"><span class="brand-dot"></span><span class="brand-name">HomeTownWork</span></div>
    </header>

    <main class="content">
      <h2 class="section-heading">LIST <span class="accent">DATA</span></h2>
      <p class="section-subtext">Subtext here Subtext here Subtext here Subtext here Subtext here Subtext here Subtext here Subtext here Subtext here Subtext here Subtext here Subtext here Subtext here Subtext here</p>

      <ul class="agenda-list">
        <li class="agenda-item"><svg class="agenda-bullet" viewBox="0 0 34 34" aria-hidden="true"><circle cx="17" cy="17" r="14" fill="var(--item-blue)"/><circle cx="17" cy="17" r="6" fill="var(--bullet-orange)"/></svg>Volutpat in in ante id, lobortis justo dui praesent, wisi commodo suscipit libero.</li>
        <li class="agenda-item"><svg class="agenda-bullet" viewBox="0 0 34 34" aria-hidden="true"><circle cx="17" cy="17" r="14" fill="var(--item-blue)"/><circle cx="17" cy="17" r="6" fill="var(--bullet-orange)"/></svg>Volutpat in in ante id, lobortis justo dui praesent, wisi commodo suscipit libero.</li>
        <li class="agenda-item"><svg class="agenda-bullet" viewBox="0 0 34 34" aria-hidden="true"><circle cx="17" cy="17" r="14" fill="var(--item-blue)"/><circle cx="17" cy="17" r="6" fill="var(--bullet-orange)"/></svg>Volutpat in in ante id, lobortis justo dui praesent, wisi commodo suscipit libero.</li>
        <li class="agenda-item"><svg class="agenda-bullet" viewBox="0 0 34 34" aria-hidden="true"><circle cx="17" cy="17" r="14" fill="var(--item-blue)"/><circle cx="17" cy="17" r="6" fill="var(--bullet-orange)"/></svg>Volutpat in in ante id, lobortis justo dui praesent, wisi commodo suscipit libero.</li>
        <li class="agenda-item"><svg class="agenda-bullet" viewBox="0 0 34 34" aria-hidden="true"><circle cx="17" cy="17" r="14" fill="var(--item-blue)"/><circle cx="17" cy="17" r="6" fill="var(--bullet-orange)"/></svg>Volutpat in in ante id, lobortis justo dui praesent, wisi commodo suscipit libero.</li>
        <li class="agenda-item"><svg class="agenda-bullet" viewBox="0 0 34 34" aria-hidden="true"><circle cx="17" cy="17" r="14" fill="var(--item-blue)"/><circle cx="17" cy="17" r="6" fill="var(--bullet-orange)"/></svg>Volutpat in in ante id, lobortis justo dui praesent, wisi commodo suscipit libero.</li>
        <li class="agenda-item"><svg class="agenda-bullet" viewBox="0 0 34 34" aria-hidden="true"><circle cx="17" cy="17" r="14" fill="var(--item-blue)"/><circle cx="17" cy="17" r="6" fill="var(--bullet-orange)"/></svg>Volutpat in in ante id, lobortis justo dui praesent, wisi commodo suscipit libero.</li>
      </ul>
    </main>

    <footer class="slide-footer">Copyrighte@2014</footer>
  </div>
</body>
</html>
```